Blog Banner Design Project: Harbour Lantern Guides

Looking for a new banner for my blog " Owen Pelsworth's Harbour Lantern Guides" at http://www.harbourlanternguides-demo.net - and once design agreed also want an updated album art for the podcast that goes along with the site.
For more about the blog and what it is about:
http://www.harbourlanternguides-demo.net/about
Harbour Lantern Guides is a Luxury Travel Blog And Podcast that provides inspiration, advice and tips about luxurious travel experiences, including destinations, transportation, accommodation, and journeys, that travellers can read, listen to or watch.
Objective of the new design
(1) retain the colour scheme ideally to retain the brand identity, as have been using these colours since 2005.
(2) introduce more of my personality and make it more visually and overt that it is "Owen Pelsworth's Harbour Lantern Guides", so possibly introducing my image into the blog banner so visitors are clear and more aware of the person behind the brand.
(3) needs to have an up-market, luxury but modern feel.
(4) if possible reflect the focus on the content (destinations, transportation, accommodation, attractions and journeys) - but this maybe best left to just words as want the design to be bold and more of the branding and personality.
Ideal wording
Smallish: Owen Pelsworth's
Main wording: Harbour Lantern Guides
Sub-title/ small: luxurious destinations, transportation, accommodation and journeys.
I have a poll running with readers of my blog to rate the designs to help me to chose the final route, and so there is no need to submit any more designs. I will make the decision once the poll closes on the weekend.

```html
<!DOCTYPE html>
<html lang="en">
<head>
<meta charset="utf-8">
<title>Owen Pelsworth's Harbour Lantern Guides – Banner</title>
<link rel="stylesheet" href="https://fonts.googleapis.com/css2?family=Bebas+Neue&family=Open+Sans:wght@700;800&display=swap">
<style>
  :root {
    --cream: #fffaf2;
    --peach: #ffd79c;
    --orange: #f59a2c;
    --deep-orange: #e9791a;
    --purple: #6a2c8e;
    --band: #3b1848;
    --band-line: #b48fc9;
    --white: #ffffff;
    --sky-top: #6b5aa8;
    --sky-mid: #a9a6d8;
    --sea: #3fb7c4;
    --sand: #eef3f1;
    --skin: #c79a7e;
    --jacket: #2b2f45;
  }
  * { margin: 0; padding: 0; box-sizing: border-box; }
  html, body { width: 1200px; height: 172px; overflow: hidden; background: var(--white); }
  .banner {
    position: relative;
    width: 1200px;
    height: 172px;
    overflow: hidden;
    background: linear-gradient(90deg, var(--cream) 0%, var(--peach) 22%, var(--orange) 38%, var(--deep-orange) 46%);
  }
  .banner__lower {
    position: absolute; left: 0; right: 0; top: 152px; bottom: 0;
    background: linear-gradient(90deg, var(--cream), #fff1dc 40%, #d8eef0 62%, #bfe6ea 100%);
  }
  .banner__scene {
    position: absolute; left: 505px; top: 0; width: 695px; height: 172px;
    background: linear-gradient(180deg, var(--sky-top) 0%, var(--sky-mid) 52%, #9fd8e0 62%, var(--sea) 78%, var(--sand) 100%);
  }
  .banner__portrait {
    position: absolute; left: 370px; top: 0; width: 150px; height: 121px;
    background: linear-gradient(180deg, #e9b98f 0%, var(--skin) 55%, var(--jacket) 88%);
  }
  .owner-name {
    position: absolute; left: 24px; top: 4px;
    font-family: "Open Sans", sans-serif; font-weight: 800;
    font-size: 25px; letter-spacing: 1px; text-transform: uppercase;
    color: var(--purple);
    white-space: nowrap;
  }
  .site-title {
    position: absolute; left: 20px; top: 44px;
    font-family: "Bebas Neue", sans-serif; font-weight: 400;
    font-size: 80px; line-height: 1; letter-spacing: 0;
    color: var(--orange);
    white-space: nowrap;
    transform: scaleX(0.52); transform-origin: left top;
  }
  .topics-band {
    position: absolute; left: 0; top: 121px; width: 710px; height: 31px;
    background: var(--band);
    border-top: 2px solid var(--band-line);
    display: flex; align-items: center; padding-left: 14px;
  }
  .topics-band__text {
    font-family: "Open Sans", sans-serif; font-weight: 700;
    font-size: 14px; letter-spacing: 0.2px; text-transform: uppercase;
    color: var(--white); white-space: nowrap;
  }
</style>
</head>
<body>
  <header class="banner">
    <div class="banner__scene" role="img" aria-label="Photograph of a palm-covered tropical island in a turquoise sea under a purple sky"></div>
    <div class="banner__lower"></div>
    <div class="banner__portrait" role="img" aria-label="Portrait photograph of the blog's host, Owen Pelsworth"></div>
    <p class="owner-name">Owen Pelsworth's</p>
    <h1 class="site-title">Harbour Lantern Guides</h1>
    <div class="topics-band">
      <p class="topics-band__text">Luxurious destinations , transportation , accomodation &amp; journeys</p>
    </div>
  </header>
</body>
</html>
```